Website header design

Need a graphic design for a Wordpress website.

The site is based on a premium theme that client has already selected: - http://demo.plumvane.net/?name=courier

The purpose of this project is to create a header banner that includes the client picture, company name and tag line and an attractive, clean and modern looking background.

For information only: The background of site will be white or a light color

The Header should include the site name: "The Brindle Harbour Centre Ltd" and the tag line: "Tap Into Your Fullest Potential"

The client has also provided a color scheme they like( See attachment )

Banner height: 140 Pix

Target Market(s)

The audience of this site are people who are looking for solution to various health issues and consider EFT as a solution.

EFT stands for "Emotional Freedom Technique"

Industry/Entity Type

Graphic Design

Requirements
Must have
• The colors that the client has selected are very bright.
Still I would like the header to have a lot of light in it so that it does not look to bulky.

Results must be provided in a PSD file
Nice to have
• The banner can be constructed from few layers
Should not have
• No specific symbol.

```html
<!DOCTYPE html>
<html lang="en">
<head>
<meta charset="utf-8">
<title>The Brindle Harbour Centre Ltd</title>
<link href="https://fonts.googleapis.com/css2?family=Macondo&family=Noto+Serif:wght@700&display=swap" rel="stylesheet">
<style>
  :root {
    --page-bg: #f3f3f3;
    --frame: #b9e4ea;
    --sky-top: #e9e7e6;
    --sky-mid: #f6ece4;
    --sky-low: #f7d9c2;
    --sun-glow: #fffbe9;
    --title-brown: #9a4a0c;
    --tagline-teal: #17869c;
    --portrait-hair: #2a1a16;
    --portrait-coat: #7a4a2a;
    --portrait-accent: #f15a22;
  }
  * { margin: 0; padding: 0; box-sizing: border-box; }
  html, body {
    width: 1200px;
    height: 900px;
    overflow: hidden;
    background: var(--page-bg);
  }
  .site-header {
    position: absolute;
    left: 108px;
    top: 96px;
    width: 968px;
    height: 140px;
    border: 3px solid var(--frame);
    box-shadow: 0 3px 4px rgba(0, 0, 0, 0.28);
    overflow: hidden;
    background:
      radial-gradient(ellipse 260px 90px at 490px 118px, var(--sun-glow) 0%, rgba(255, 251, 233, 0) 100%),
      linear-gradient(180deg, var(--sky-top) 0%, var(--sky-mid) 55%, var(--sky-low) 100%);
  }
  .site-title {
    position: absolute;
    left: 0;
    top: 28px;
    width: 886px;
    text-align: center;
    font-family: "Macondo", cursive;
    font-size: 36px;
    font-weight: 400;
    letter-spacing: 0.5px;
    color: var(--title-brown);
    text-shadow: 2px 3px 4px rgba(120, 80, 40, 0.35);
    white-space: nowrap;
  }
  .site-tagline {
    position: absolute;
    left: 0;
    top: 82px;
    width: 886px;
    text-align: center;
    font-family: "Noto Serif", serif;
    font-weight: 700;
    font-size: 17px;
    letter-spacing: 0.3px;
    color: var(--tagline-teal);
    text-shadow: 0 0 3px #ffffff, 0 0 3px #ffffff;
  }
  .client-portrait {
    position: absolute;
    left: 762px;
    top: 0;
    width: 92px;
    height: 137px;
    background: linear-gradient(180deg, var(--portrait-hair) 0%, var(--portrait-hair) 40%, var(--portrait-coat) 65%, var(--portrait-accent) 100%);
    border-radius: 40px 40px 0 0;
  }
</style>
</head>
<body>
  <header class="site-header">
    <h1 class="site-title">THE BRINDLE HARBOUR CENTRE LTD</h1>
    <p class="site-tagline">Tap into Your Fullest Potencial</p>
    <div class="client-portrait" role="img" aria-label="Photograph of the smiling practitioner in a brown cardigan and orange top"></div>
  </header>
</body>
</html>
```